New Web Design Project (Blog, Video Blog and Education)

I have a domain www.brightlatticehub.tv I am looking for a website to post blogs and develop a site like https://tinkerandventure.com/ initially blogs then moving into video podcasting as we gain traction. The idea of www.brightlatticehub.tv is that it is about the connection to people, businesses and ideas that change the world.

Target Market(s)

This is a Blog, Podcast site with training material on it targeted at people who want access to connections and simple information on topics they are interested in.

Coding

Coded - Design and coding required

Number of Pages Required

4 page

Font styles to use
Other font styles liked:
• century gothic

Colors
ec1f27
5c5c5c
ffffff

Requirements
Must have
• Really good usability and A nice clean design that looks simple professional and compelling look at, not too busy and clear obvious navigation.
Nice to have
• Magical attraction to visitors.
Should not have
• Clunky design or poor usability

```html
<!DOCTYPE html>
<html lang="en">
<head>
<meta charset="utf-8">
<title>BrightLattice — Build Your Online Business</title>
<link href="https://fonts.googleapis.com/css2?family=Mulish:wght@400;700;800&display=swap" rel="stylesheet">
<style>
:root{
  --red:#ec1f27;
  --gray:#5c5c5c;
  --gray-deep:#3d3d3d;
  --white:#ffffff;
  --ink:#2b2b2b;
  --muted:#7a7a7a;
  --badge:#d9d9d9;
  --rule:#ececec;
  --field:#f3f3f3;
  --quote:#e8e8e8;
}
*{box-sizing:border-box;margin:0;padding:0}
html,body{width:1200px;height:2486px;overflow:hidden;background:var(--white)}
body{position:relative;font-family:"Mulish","Century Gothic",Arial,sans-serif;color:var(--ink)}
.abs{position:absolute}

/* Hero */
.hero{left:0;top:0;width:1200px;height:721px;background:var(--gray-deep)}
.brand{left:108px;top:22px;display:flex;align-items:center;gap:14px;color:var(--white);font-weight:800;font-size:21px;letter-spacing:.3px;white-space:nowrap}
.brand-mark{width:44px;height:44px;border-radius:50%;background:var(--white)}
.nav{top:37px;color:var(--white);font-size:13px;letter-spacing:.5px;white-space:nowrap}
.nav-home{font-weight:800}
.nav-contact{left:953px;top:27px;width:137px;height:38px;background:var(--red);color:var(--white);font-size:13px;display:flex;align-items:center;justify-content:center;letter-spacing:.5px}
.hero-title{left:108px;top:268px;width:520px;color:var(--white);font-weight:800;font-size:38px;line-height:46px;white-space:nowrap}
.hero-lede{left:108px;top:428px;width:500px;color:var(--white);font-size:16px;line-height:25px;white-space:nowrap}
.hero-cue{left:108px;top:501px;color:var(--white);font-size:12px;letter-spacing:.2px;white-space:nowrap}
.email-field{left:108px;top:540px;width:273px;height:50px;background:var(--field);color:var(--muted);font-size:12px;padding-left:16px;display:flex;align-items:center}
.email-button{left:394px;top:540px;width:203px;height:50px;background:var(--red);color:var(--white);font-size:13px;font-weight:700;display:flex;align-items:center;justify-content:center}
.portrait-frame{left:691px;top:124px;width:399px;height:560px;background:var(--white);padding:13px}
.portrait{width:100%;height:100%;background:linear-gradient(160deg,#e3e7ea 0%,#bfc9d2 40%,#34598f 75%,#213f70 100%)}

/* Featured */
.featured-label{left:0;top:789px;width:1200px;text-align:center;font-size:12px;color:var(--gray);letter-spacing:1px}
.badge{top:846px;height:34px;background:var(--badge);border-radius:4px}

/* Tiles */
.tile{top:973px;width:317px;height:202px}
.tile-photo{width:100%;height:170px}
.tile-label{height:32px;background:var(--red);color:var(--white);font-size:13px;font-weight:700;display:flex;align-items:center;justify-content:center;letter-spacing:.5px}
.warm{background:linear-gradient(135deg,#c9b59a 0%,#8c7a68 50%,#50535a 100%)}
.cool{background:linear-gradient(135deg,#6b5a6c 0%,#9a8aa0 45%,#c9bfc6 100%)}
.desk{background:linear-gradient(135deg,#9a7a56 0%,#d2d0cc 50%,#6f6a66 100%)}

.rule{left:58px;width:1085px;height:1px;background:var(--rule)}

/* Testimonials */
.section-title{left:0;width:1200px;text-align:center;font-weight:800;color:var(--ink)}
.testimonial-title{top:1370px;font-size:29px}
.quote-mark{top:1418px;font-size:190px;line-height:1;color:var(--quote);font-weight:800;font-family:Georgia,serif}
.quote-text{left:186px;top:1472px;width:828px;text-align:center;font-size:18px;line-height:30px;color:var(--ink);white-space:nowrap}
.quote-dash{left:584px;top:1571px;width:32px;height:2px;background:var(--gray)}
.quote-author{left:0;top:1588px;width:1200px;text-align:center;font-size:13px;font-weight:700;letter-spacing:1px;color:var(--gray)}

/* Posts */
.posts-kicker{left:0;top:1804px;width:1200px;text-align:center;font-size:12px;font-weight:700;color:var(--red);letter-spacing:.5px}
.posts-title{top:1830px;font-size:27px;line-height:40px;white-space:nowrap}
.post{top:1952px;width:278px;height:355px;border:1px solid #efefef;background:var(--white)}
.post-photo{width:100%;height:166px;position:relative}
.post-title{position:absolute;left:25px;top:198px;font-size:16px;font-weight:700;line-height:21px;white-space:nowrap;color:var(--ink)}
.read-more{position:absolute;left:25px;font-size:12px;font-weight:700;color:var(--red)}
.post-date{position:absolute;left:17px;top:328px;font-size:12px;color:var(--gray);display:flex;align-items:center;gap:7px}
.post-date i{width:9px;height:10px;border:1px solid var(--gray);display:block}
.play{position:absolute;left:112px;top:56px}

/* Footer */
.footer{left:0;top:2403px;width:1200px;height:83px;background:var(--gray);color:var(--white)}
.footer-text{position:absolute;left:108px;top:31px;font-size:14px;white-space:nowrap}
.social{position:absolute;top:33px;width:18px;height:18px;border-radius:50%;background:var(--white)}
</style>
</head>
<body>

<header class="abs hero">
  <div class="abs brand"><span class="brand-mark"></span>BRIGHTLATTICE</div>
  <nav>
    <span class="abs nav nav-home" style="left:543px">HOME</span>
    <span class="abs nav" style="left:644px">ABOUT</span>
    <span class="abs nav" style="left:751px">SERVICES</span>
    <span class="abs nav" style="left:873px">BLOG</span>
    <span class="abs nav-contact">CONTACT</span>
  </nav>
  <h1 class="abs hero-title">ARE YOU READY TO<br>BUILD YOUR ONLINE<br>BUSINESS?</h1>
  <p class="abs hero-lede">Lorem ipsum dolor sit amet, consectetuer adipiscing elit.<br>Aenean commodo ligula eget dolor. Aenean massa.</p>
  <p class="abs hero-cue">IT ALL STARTS WITH ONE SIMPLE ACTION. DROP YOUR EMAIL BELOW.</p>
  <div class="abs email-field">type your email</div>
  <div class="abs email-button">Let Me In!</div>
  <div class="abs portrait-frame">
    <div class="portrait" role="img" aria-label="Portrait of a smiling businessman in a blue suit"></div>
  </div>
</header>

<section>
  <p class="abs featured-label">FEATURED IN</p>
  <div class="abs badge" style="left:112px;width:106px"></div>
  <div class="abs badge" style="left:271px;width:108px"></div>
  <div class="abs badge" style="left:431px;width:170px"></div>
  <div class="abs badge" style="left:655px;width:92px"></div>
  <div class="abs badge" style="left:805px;width:77px"></div>
  <div class="abs badge" style="left:932px;width:156px"></div>
</section>

<section>
  <div class="abs tile" style="left:108px">
    <div class="tile-photo warm" role="img" aria-label="Team working together around a laptop"></div>
    <div class="tile-label">START HERE</div>
  </div>
  <div class="abs tile" style="left:441px">
    <div class="tile-photo cool" role="img" aria-label="Hands typing on a keyboard"></div>
    <div class="tile-label">BUSINESS BLOG</div>
  </div>
  <div class="abs tile" style="left:772px">
    <div class="tile-photo desk" role="img" aria-label="Desk with charts, calculator and laptop"></div>
    <div class="tile-label">BUSINESS TOOLS</div>
  </div>
</section>

<div class="abs rule" style="top:1269px"></div>

<section>
  <h2 class="abs section-title testimonial-title">Testimonials</h2>
  <span class="abs quote-mark" style="left:140px">&ldquo;</span>
  <span class="abs quote-mark" style="left:980px">&rdquo;</span>
  <p class="abs quote-text">Lorem ipsum dolor sit amet, consectetur adipisicing elit, sed do eiusmod tempor incididunt ut<br>labore et dolore magna aliqua.</p>
  <div class="abs quote-dash"></div>
  <p class="abs quote-author">JOHN DOE</p>
</section>

<div class="abs rule" style="top:1710px"></div>

<section>
  <p class="abs posts-kicker">LATEST POSTS</p>
  <h2 class="abs section-title posts-title">STARTING AN ONLINE BUSINESS: YOUR DEFINITIVE<br>RESOURCE TO PASSIVE INCOME</h2>

  <article class="abs post" style="left:151px">
    <div class="post-photo desk" role="img" aria-label="Desk with charts and a tablet"></div>
    <h3 class="post-title">Lorem ipsum<br>dolor sit amet</h3>
    <span class="read-more" style="top:252px">Read More</span>
    <span class="post-date"><i></i>Mar 15, 2019</span>
  </article>

  <article class="abs post" style="left:461px">
    <div class="post-photo warm" role="img" aria-label="Team meeting around a laptop">
      <svg class="play" width="52" height="52" viewBox="0 0 52 52"><circle cx="26" cy="26" r="26" fill="#ec1f27"/><path d="M20 15 L38 26 L20 37 Z" fill="#fff"/></svg>
    </div>
    <h3 class="post-title">Incididunt ut labore et<br>dolore magna aliqua. Ut<br>enim ad minim veniam</h3>
    <span class="read-more" style="top:273px">Read More</span>
    <span class="post-date"><i></i>Mar 14, 2019</span>
  </article>

  <article class="abs post" style="left:771px">
    <div class="post-photo cool" role="img" aria-label="Hands typing on a keyboard"></div>
    <h3 class="post-title">Lorem ipsum dolor sit<br>amet, consectetur</h3>
    <span class="read-more" style="top:252px">Read More</span>
    <span class="post-date"><i></i>Mar 13, 2019</span>
  </article>
</section>

<footer class="abs footer">
  <p class="footer-text">© 2019 BrightLattice Hub. | Privacy Policy | Terms and Conditions</p>
  <span class="social" style="left:892px"></span>
  <span class="social" style="left:936px"></span>
  <span class="social" style="left:981px"></span>
  <span class="social" style="left:1027px"></span>
  <span class="social" style="left:1072px"></span>
</footer>

</body>
</html>
```